Web Design Project for an operational risk management consulting company

Website is for a consulting company specialising in operational risk management. Our specialist areas include crisis and emergency management, community engagement, safety and security. We work internationally, generally in high hazard environments. We are a highly ethical and professional company which prides itself on delivering a strong level of customer service.

As a company we recognise that the key to keeping people safe is ensuring that they work in an ethical and sustainable manner. Therefore we are as much about soft skills as we are about hard skills. We would like our website and supporting images to reflect this.
We have worked throughout Africa and the Middle east, as well as Asia pacific. An international flavour to the website would also be great.
Background images on www.corvellpartnersglobal.example are a good example of what we are thinking of, though very open to fresh ideas.

Target Market(s)

Our customers are generally medium to large organisations who work internationally. We would like to also support more not for profits and non government organisations who work in hazardous environments

Industry/Entity Type

It Company

Number of Pages Required

5+ page

Font styles to use
Sans Serif

Requirements
Must have
• Easy to edit by non IT people
• Section for blogs/news updates
• Pages should include:
• (A) home page
• (B) about us
• (C) services
• (D) contact
• (E) insights
Nice to have
• An international and professional theme. Some gritty images that symbolise the risks associated with working in unstable environments, as well as some human ones and that of the environment
Should not have
• Cartoonish or generic images
• Not focus on traditional physical security aspects

```html
<!DOCTYPE html>
<html lang="en">
<head>
<meta charset="utf-8">
<title>Halvern Risk — Operational Risk Management</title>
<link rel="stylesheet" href="https://fonts.googleapis.com/css2?family=Oswald:wght@500&family=Open+Sans:wght@300;400;600;700&family=Roboto:wght@400;500&display=swap">
<style>
:root{
  --navy:#0c3d62;
  --navy-deep:#0a3354;
  --blue:#1f6fa3;
  --ink:#333b44;
  --muted:#6b737b;
  --grey-band:#dcdde0;
  --white:#ffffff;
  --sky-top:#c9d3dc;
  --sky-mid:#8f9eab;
  --city:#3e4a56;
}
*{box-sizing:border-box;margin:0;padding:0}
html,body{width:889px;height:1200px;overflow:hidden;background:var(--white)}
body{font-family:"Open Sans",Arial,sans-serif;color:var(--ink);position:relative}

.site-header{position:absolute;left:0;top:0;width:889px;height:112px;background:var(--white)}
.brand{position:absolute;left:30px;top:28px;display:flex;align-items:center;gap:12px}
.brand-dot{width:48px;height:48px;border-radius:50%;background:var(--navy)}
.brand-name{font-family:"Open Sans",Arial,sans-serif;font-weight:700;font-size:28px;color:var(--navy)}
.main-nav{position:absolute;right:22px;top:44px;display:flex;gap:8px}
.main-nav a{font-family:"Roboto",Arial,sans-serif;font-size:14px;color:var(--muted);text-decoration:none;padding:8px 22px;border-radius:20px;border:2px solid transparent;letter-spacing:.5px}
.main-nav a.active{border-color:var(--navy);color:var(--navy);font-weight:500}

.hero{position:absolute;left:0;top:112px;width:889px;height:470px;background:linear-gradient(180deg,var(--sky-top) 0%,var(--sky-mid) 45%,var(--city) 100%)}
.hero-text{position:absolute;left:0;top:170px;width:889px;text-align:center;color:var(--white)}
.hero-title{font-family:"Oswald",Arial,sans-serif;font-weight:500;font-size:46px;letter-spacing:1px;text-shadow:0 2px 6px rgba(0,0,0,.35)}
.hero-sub{font-family:"Open Sans",Arial,sans-serif;font-size:30px;margin-top:2px;text-shadow:0 2px 6px rgba(0,0,0,.35)}

.services{position:absolute;left:50px;top:460px;width:789px;display:flex;justify-content:space-between}
.service-card{width:237px;height:250px;position:relative}
.service-body{position:absolute;left:0;top:42px;width:237px;height:208px;background:var(--navy);border-radius:4px;padding:64px 18px 0;color:var(--white);text-align:center}
.service-icon{position:absolute;left:78px;top:0;width:82px;height:82px;border-radius:50%;background:var(--navy);border:4px solid var(--white);display:flex;align-items:center;justify-content:center}
.service-title{font-size:19px;font-weight:400;line-height:1.2;margin-bottom:10px}
.service-text{font-size:11.5px;line-height:1.5;color:#d6e1ea;text-align:left}

.welcome{position:absolute;left:0;top:735px;width:889px;text-align:center}
.welcome-title{font-weight:300;font-size:40px;color:var(--ink)}
.welcome-title span{color:var(--blue);font-weight:400}
.welcome-text{width:720px;margin:18px auto 0;font-size:12.5px;line-height:1.6;color:var(--muted)}

.blog{position:absolute;left:0;top:930px;width:889px;height:225px;background:var(--grey-band)}
.blog-heading{text-align:center;font-weight:300;font-size:34px;margin-top:18px;color:var(--ink)}
.blog-heading span{color:var(--blue);font-weight:400}
.posts{display:flex;justify-content:space-between;width:820px;margin:22px auto 0}
.post{width:250px;display:flex;gap:12px}
.post-date{width:60px;height:62px;background:var(--navy);color:var(--white);text-align:center;flex:none}
.post-day{display:block;font-size:26px;font-weight:700;line-height:38px}
.post-month{display:block;font-size:13px;background:var(--navy-deep);line-height:24px}
.post-title{font-size:13px;font-weight:700;color:var(--navy);line-height:1.3}
.post-text{font-size:11px;color:var(--muted);line-height:1.4;margin-top:4px}
.post-more{display:inline-block;margin-top:6px;font-size:11px;font-weight:700;color:var(--navy);text-decoration:underline}

.site-footer{position:absolute;left:0;top:1155px;width:889px;height:45px;background:var(--navy);display:flex;align-items:center;justify-content:space-between;padding:0 34px;color:var(--white);font-size:12px}
.site-footer strong{font-weight:700}
.social{display:flex;gap:14px}
.social span{width:16px;height:16px;border-radius:50%;background:#c6d4e0}
</style>
</head>
<body>

<header class="site-header">
  <div class="brand">
    <span class="brand-dot"></span>
    <span class="brand-name">Halvern Risk</span>
  </div>
  <nav class="main-nav">
    <a class="active" href="#">HOME</a>
    <a href="#">ABOUT</a>
    <a href="#">SERVICES</a>
    <a href="#">CONTACT</a>
    <a href="#">INSIGHTS</a>
  </nav>
</header>

<section class="hero" role="img" aria-label="Hazy skyline of a large city with tall towers under a pale sky">
  <div class="hero-text">
    <h1 class="hero-title">OPERATIONAL RISK MANAGEMENT</h1>
    <p class="hero-sub">Ethical And Sustainable Manner</p>
  </div>
</section>

<section class="services">
  <article class="service-card">
    <div class="service-body">
      <h2 class="service-title">Crisis and emergency management</h2>
      <p class="service-text">Lorem Ipsum is simply dummy text of the printing and typesetting industry. Lorem Ipsum has been the industry.</p>
    </div>
    <div class="service-icon">
      <svg width="40" height="40" viewBox="0 0 40 40" aria-hidden="true"><path d="M20 5 L37 34 H3 Z" fill="none" stroke="#fff" stroke-width="3" stroke-linejoin="round"/><rect x="18.5" y="14" width="3" height="11" fill="#fff"/><circle cx="20" cy="29" r="1.8" fill="#fff"/></svg>
    </div>
  </article>
  <article class="service-card">
    <div class="service-body">
      <h2 class="service-title">Community Engagement</h2>
      <p class="service-text">Lorem Ipsum is simply dummy text of the printing and typesetting industry. Lorem Ipsum has been the industry.</p>
    </div>
    <div class="service-icon">
      <svg width="44" height="40" viewBox="0 0 44 40" aria-hidden="true"><circle cx="22" cy="12" r="6" fill="#fff"/><circle cx="9" cy="16" r="4.5" fill="#fff"/><circle cx="35" cy="16" r="4.5" fill="#fff"/><path d="M12 34 a10 10 0 0 1 20 0 Z" fill="#fff"/><path d="M1 33 a8 8 0 0 1 13 -6 l-2 6 Z" fill="#fff"/><path d="M43 33 a8 8 0 0 0 -13 -6 l2 6 Z" fill="#fff"/></svg>
    </div>
  </article>
  <article class="service-card">
    <div class="service-body">
      <h2 class="service-title">Safety and Security</h2>
      <p class="service-text">Lorem Ipsum is simply dummy text of the printing and typesetting industry. Lorem Ipsum has been the industry.</p>
    </div>
    <div class="service-icon">
      <svg width="38" height="40" viewBox="0 0 38 40" aria-hidden="true"><path d="M19 3 L34 9 V19 C34 28 27 34 19 37 C11 34 4 28 4 19 V9 Z" fill="#fff"/><path d="M12 20 L17 25 L26 14" fill="none" stroke="#0c3d62" stroke-width="3.5" stroke-linecap="round" stroke-linejoin="round"/></svg>
    </div>
  </article>
</section>

<section class="welcome">
  <h2 class="welcome-title">Welcome to <span>Halvern Risk</span></h2>
  <p class="welcome-text">Lorem Ipsum is simply dummy text of the printing and typesetting industry. Lorem Ipsum has been the industry's standard dummy text ever since the 1500s, when an unknown printer took a galley of type and scrambled it to make a type specimen book.</p>
</section>

<section class="blog">
  <h2 class="blog-heading">Latest <span>Blog</span></h2>
  <div class="posts">
    <article class="post">
      <div class="post-date"><span class="post-day">16</span><span class="post-month">Sep</span></div>
      <div>
        <h3 class="post-title">Lorem Ipsum is simply dummy text of the print</h3>
        <p class="post-text">Lorem Ipsum is simply dummy text of the printing and typesetting industry.</p>
        <a class="post-more" href="#">READ MORE</a>
      </div>
    </article>
    <article class="post">
      <div class="post-date"><span class="post-day">15</span><span class="post-month">Sep</span></div>
      <div>
        <h3 class="post-title">Lorem Ipsum is simply dummy text of the print</h3>
        <p class="post-text">Lorem Ipsum is simply dummy text of the printing and typesetting industry.</p>
        <a class="post-more" href="#">READ MORE</a>
      </div>
    </article>
    <article class="post">
      <div class="post-date"><span class="post-day">14</span><span class="post-month">Sep</span></div>
      <div>
        <h3 class="post-title">Lorem Ipsum is simply dummy text of the print</h3>
        <p class="post-text">Lorem Ipsum is simply dummy text of the printing and typesetting industry.</p>
        <a class="post-more" href="#">READ MORE</a>
      </div>
    </article>
  </div>
</section>

<footer class="site-footer">
  <p>© <strong>HALVERN RISK</strong> - 2015. All rights reserved.</p>
  <div class="social"><span></span><span></span><span></span></div>
</footer>

</body>
</html>
```